QR Business Card

Design a vertical orientation business card with approved logo and fonts (Jubilee Lines and Aviano). Use metallic gold and black, embossing parts of the logo.
Perhaps color back of card black?
Address:
5873 Harlow Crescent
Level 2
North Cove Harbor FL 32084

Delia Porcaro
Managing Partner

Industry/Entity Type

Business

```html
<!DOCTYPE html>
<html lang="en">
<head>
<meta charset="utf-8">
<title>Quarter Reef – Business Card</title>
<link rel="stylesheet" href="https://fonts.googleapis.com/css2?family=Open+Sans:wght@400;700&display=swap">
<style>
  :root {
    --backdrop: #e6e3de;
    --card: #ffffff;
    --card-edge: #2b2b2b;
    --gold: #fccd3f;
    --ink: #222222;
    --ink-soft: #3a3a3a;
  }
  html, body {
    margin: 0;
    padding: 0;
    width: 1200px;
    height: 1022px;
    overflow: hidden;
    background: var(--backdrop);
    font-family: "Open Sans", Arial, sans-serif;
    color: var(--ink);
  }
  .canvas {
    position: relative;
    width: 1200px;
    height: 1022px;
  }
  .card {
    position: absolute;
    top: 51px;
    height: 897px;
    background: var(--card);
    border: 2px solid var(--card-edge);
    box-sizing: border-box;
    overflow: hidden;
  }
  .card--front { left: 53px; width: 517px; }
  .card--back  { left: 638px; width: 514px; }

  .brand-band {
    position: absolute;
    left: 0; top: 0;
    width: 100%;
    height: 146px;
    background: var(--gold);
  }
  .brand-rule {
    position: absolute;
    left: 0; top: 150px;
    width: 100%;
    height: 3px;
    background: var(--ink);
  }
  .brand-square {
    position: absolute;
    left: 144px; top: 34px;
    width: 218px; height: 193px;
    background: var(--card);
  }
  .brand-name {
    position: absolute;
    left: 0; top: 244px;
    width: 100%;
    text-align: center;
    font-size: 32px;
    font-weight: 700;
    letter-spacing: 6px;
    color: var(--ink);
    margin: 0;
  }
  .brand-tagline {
    position: absolute;
    left: 0; top: 284px;
    width: 100%;
    text-align: center;
    font-size: 28px;
    font-variant: small-caps;
    letter-spacing: 3px;
    color: var(--ink);
    margin: 0;
  }
  .person { position: absolute; left: 0; top: 452px; width: 100%; text-align: center; }
  .person__name { margin: 0; font-size: 33px; font-weight: 700; color: var(--ink-soft); }
  .person__role { margin: -2px 0 0; font-size: 23px; letter-spacing: 0.5px; color: var(--ink-soft); }

  .contact {
    position: absolute; left: 0; top: 622px; width: 100%;
    list-style: none; margin: 0; padding: 0;
    text-align: center; font-size: 27px; color: var(--ink-soft);
  }
  .contact li { display: flex; justify-content: center; align-items: center; gap: 10px; height: 47px; }
  .contact svg { width: 26px; height: 26px; }

  .address {
    position: absolute; left: 0; top: 758px; width: 100%;
    text-align: center; font-style: normal; font-size: 25px; line-height: 41px;
    color: var(--ink-soft);
  }
</style>
</head>
<body>
<main class="canvas">
  <section class="card card--front">
    <div class="brand-band"></div>
    <div class="brand-rule"></div>
    <div class="brand-square"></div>
    <h1 class="brand-name">QUARTER REEF</h1>
    <p class="brand-tagline">Design Studio</p>

    <div class="person">
      <h2 class="person__name">Delia Porcaro</h2>
      <p class="person__role">Managing Partner</p>
    </div>

    <ul class="contact">
      <li>
        <svg viewBox="0 0 26 26" aria-hidden="true">
          <circle cx="13" cy="13" r="12" fill="var(--gold)"/>
          <path d="M9 7 l3 0 1 4 -2 1.5 q1.5 3 4 4 l1.5 -2 4 1 0 3 q-1 1 -3 1 q-9 -2 -10 -10 q0 -2 1.5 -2.5z" fill="#fff"/>
        </svg>
        <span>012-555-0147</span>
      </li>
      <li>
        <svg viewBox="0 0 26 26" aria-hidden="true">
          <rect x="1" y="6" width="24" height="16" rx="4" fill="var(--gold)"/>
          <path d="M4 9 l9 7 9 -7" fill="none" stroke="#fff" stroke-width="2"/>
        </svg>
        <span>info@quarterreef.com</span>
      </li>
    </ul>

    <address class="address">
      5873 Harlow Crescent, Level 2<br>
      North Cove Harbor FL 32084
    </address>
  </section>

  <section class="card card--back" aria-label="Card back"></section>
</main>
</body>
</html>
```